Pale Lanterns Old Lane Walk Poster Design

We need an A4 sized poster to promote our weekly true crime tours. This poster will be posted onto community noticeboards.
Lots of information and images can be viewed at the following links:-
www.palelanterns.com.au
www.palelanterns.com.au/bookings/
https://www.facebook.com/palelanternsoldlane/
https://www.examplereviews.com.au/Attraction_Review-g000000-d00000000-Reviews-Pale_Lanterns-Newcastle_Greater_Newcastle_New_South_Wales.html
There are also a number of images for possible use at the following link - we are open to intepretation:-
http://palelanterns.com.au/tour-photographs/
The font on our website is "SpecialElite" so we would like to continue using that font type.
Target Market(s)
Adults 25-65.
Font styles to use
Other font styles liked:
- Special Elite
Colors
Designer to choose colors to be used in the design.
Look and feel
Each slider illustrates characteristics of the customer's brand and the style your logo design should communicate.

```html
<!DOCTYPE html>
<html lang="en">
<head>
<meta charset="utf-8">
<title>Pale Lanterns Old Lane Walk Poster</title>
<link href="https://fonts.googleapis.com/css2?family=Special+Elite&display=swap" rel="stylesheet">
<style>
  :root {
    --stage: #141414;
    --red: #e0332d;
    --ink: #1d1d1d;
    --panel: #1f1f1f;
    --paper-light: #d2b58a;
    --paper-mid: #b8946a;
    --paper-dark: #9a5e45;
    --white: #ffffff;
    --type: "Special Elite", "Courier New", monospace;
  }
  * { box-sizing: border-box; margin: 0; padding: 0; }
  html, body {
    width: 1200px; height: 800px; overflow: hidden;
    background: var(--stage);
    font-family: var(--type);
  }
  .poster {
    position: absolute;
    left: 330px; top: 20px;
    width: 680px; height: 958px;
    transform: scale(0.7933);
    transform-origin: top left;
    overflow: hidden;
  }
  .poster-art { position: absolute; inset: 0; width: 680px; height: 958px; }
  .poster-text { position: absolute; font-family: var(--type); line-height: 1.25; white-space: nowrap; }

  .tagline { left: 12px; top: 10px; color: var(--white); font-size: 19px; }
  .brand-name { left: 300px; top: 74px; color: var(--ink); font-size: 22px; }

  .claims { left: 440px; top: 118px; width: 230px; text-align: center; }
  .claims .percent { color: var(--white); font-size: 56px; line-height: 1; display: block; }
  .claims .word { color: var(--red); display: block; line-height: 1.05; }
  .claims .word-true { font-size: 54px; margin-bottom: 26px; }
  .claims .word-unbelievable { font-size: 28px; margin-top: 4px; }
  .claims .invite { color: var(--white); font-size: 19px; margin-top: 22px; line-height: 1.3; }

  .headline { left: 17px; top: 418px; color: var(--white); font-size: 28px; line-height: 1.2; font-weight: normal; }

  .highlights { left: 12px; top: 490px; list-style: none; color: var(--ink); font-size: 18px; }
  .highlights li { position: relative; margin-bottom: 25px; line-height: 24px; }
  .highlights li::before {
    content: ""; position: absolute; left: -5px; top: 9px;
    width: 5px; height: 5px; border-radius: 50%; background: var(--red);
  }

  .price { left: 445px; top: 608px; width: 170px; text-align: center; color: var(--white); }
  .price .amount { font-size: 72px; line-height: 1; }
  .price .currency { font-size: 34px; vertical-align: top; position: relative; top: 4px; }
  .price .duration { display: block; font-size: 22px; margin-top: -4px; }

  .contact { right: 6px; top: 918px; color: var(--white); font-size: 15px; text-align: right; line-height: 1.3; }
</style>
</head>
<body>
  <div class="poster">
    <svg class="poster-art" viewBox="0 0 680 958" xmlns="http://www.w3.org/2000/svg">
      <defs>
        <linearGradient id="paper-tone" x1="0" y1="0" x2="0.4" y2="1">
          <stop offset="0" stop-color="#d2b58a"/>
          <stop offset="0.55" stop-color="#b8946a"/>
          <stop offset="1" stop-color="#9a5e45"/>
        </linearGradient>
        <linearGradient id="street-tone" x1="0" y1="0" x2="0" y2="1">
          <stop offset="0" stop-color="#8c8c8c"/>
          <stop offset="0.5" stop-color="#4a4a4a"/>
          <stop offset="1" stop-color="#6e6e6e"/>
        </linearGradient>
      </defs>

      <rect class="paper" x="0" y="0" width="680" height="958" fill="url(#paper-tone)"/>

      <polygon class="street-photo" role="img"
               aria-label="Black and white photograph of a tram on a rainy old city street with a lone walker"
               points="0,68 455,120 372,390 0,415" fill="url(#street-tone)"/>

      <polygon class="top-band" points="0,0 680,0 455,120 0,68" fill="#e0332d"/>

      <polygon class="claims-panel" points="455,120 680,0 680,560 600,588 372,390" fill="#1f1f1f"/>

      <g class="price-drip" fill="#e0332d">
        <circle cx="528" cy="640" r="85"/>
        <rect x="472" y="660" width="24" height="130" rx="12"/>
        <rect x="500" y="660" width="27" height="112" rx="13"/>
        <rect x="570" y="660" width="26" height="136" rx="13"/>
      </g>

      <rect class="bottom-band" x="0" y="888" width="680" height="70" fill="#e0332d"/>
      <circle class="bottom-seal" cx="345" cy="885" r="64" fill="#e0332d"/>
    </svg>

    <p class="poster-text tagline">Stories the city<br>tried to forget...</p>
    <p class="poster-text brand-name">Pale Lanterns</p>

    <div class="poster-text claims">
      <span class="percent">100%</span>
      <span class="word word-true">TRUE</span>
      <span class="percent">100%</span>
      <span class="word word-unbelievable">UNBELIEVABLE</span>
      <p class="invite">Take a walk on<br>the Dark Side...</p>
    </div>

    <h1 class="poster-text headline">Revisit the scenes<br>of the crimes:</h1>

    <ul class="poster-text highlights">
      <li>Retrace the steps of Newcastle's most<br>infamous murderers.</li>
      <li>Descend into the murky world of<br>fraudsters, adulterers and lordly<br>impersonators.</li>
      <li>Unearth the keys to the heart of the<br>Tomahawk Murderer.</li>
      <li>Relive a time that proves truth is far<br>stranger than fiction.</li>
      <li>Book your ticket for a unique<br>investigation into a dark<br>and crime ridden history.</li>
    </ul>

    <div class="poster-text price">
      <span class="amount">34</span><span class="currency">AU$</span>
      <span class="duration">90 mins</span>
    </div>

    <p class="poster-text contact">Phone: 0400123987<br>Email: info@palelanterns.com.au</p>
  </div>
</body>
</html>
```